Powerpoint visual improvements

I need a cover page, and our beliefs page and differentiating factors page / graphic design for our presentation. For the cover page I would just like an attractive design that incorporate our architectural concept with columns and potentially our logo. For the beliefs page I just want a more attractive presentatoin of the concepts. For the differentiating factors page I want a graphic that captures the points about how we are different from competitors. I have used the attached content to date, but I think it can be improved. The text is included in the graphic and I would also like to make sure the firm logo is incorporated.

Target Market(s)

Individual and institutional investors.

Industry/Entity Type

Investment Advisory

Requirements
Must have
• Our corporate colors are generally RGB 145,148,149; 66,68,76; 0,0,153; and 0,63,127. Our logo is attached. Our primary font is Georgia. Our website is www.PelmarCW.com. The key pages are www.PelmarCW.com/beliefs and www.PelmarCW.com/value we are trying to capture in a presentation. We also need a new presentation cover. Use the website as a reference for the type of imagery we like.

```html
<!DOCTYPE html>
<html lang="en">
<head>
<meta charset="utf-8">
<title>Pelmar Capital Wealth – Presentation Slides</title>
<link href="https://fonts.googleapis.com/css2?family=Gelasio:wght@400;700&display=swap" rel="stylesheet">
<style>
  :root {
    --gray: #919495;
    --charcoal: #42444c;
    --royal: #000099;
    --navy: #003f7f;
    --bright: #2a3cf5;
    --sky: #1f7be3;
    --white: #ffffff;
    --canvas: #ffffff;
    --ink-blue: #1c3f8c;
  }
  * { box-sizing: border-box; margin: 0; padding: 0; }
  html, body { width: 1200px; height: 3000px; overflow: hidden; background: var(--canvas); }
  body { position: relative; font-family: "Gelasio", Georgia, serif; }

  .slide {
    position: absolute; left: 176px; width: 848px; height: 480px;
    overflow: hidden; box-shadow: 0 3px 10px rgba(0,0,0,.35);
  }
  .slide--1 { top: 10px; }
  .slide--2 { top: 510px; }
  .slide--3 { top: 1010px; }
  .slide--4 { top: 1510px; }
  .slide--5 { top: 2010px; }
  .slide--6 { top: 2510px; }

  /* photo placeholders: soft gradients in the colonnade's tones */
  .photo { position: absolute; inset: 0; }
  .photo--blue {
    background:
      linear-gradient(160deg, rgba(10,30,80,0) 0%, rgba(10,30,80,.25) 55%, rgba(10,30,80,0) 100%),
      linear-gradient(90deg,
        #22569f 0%, #3767ad 6%, #22559d 12%, #3f6fb2 20%, #24579f 28%,
        #4a76b4 38%, #2a5ba2 46%, #5680b8 56%, #2f60a5 64%,
        #7d8fb0 76%, #9aa0ae 88%, #a6a8ad 100%);
  }
  .photo--royal {
    background:
      linear-gradient(180deg, rgba(255,255,255,.06) 0%, rgba(0,0,40,.18) 100%),
      linear-gradient(90deg,
        #8e8b97 0%, #a19ea6 10%, #8c899a 20%, #3d34b8 27%, #2218b2 34%,
        #2e26bb 42%, #1b14ae 50%, #2a22b8 58%, #1a13ad 68%,
        #2820b6 78%, #1b14ac 88%, #2a22b6 100%);
  }
  .photo--gray {
    background:
      linear-gradient(180deg, rgba(255,255,255,.12) 0%, rgba(0,0,0,0) 50%, rgba(0,0,0,.08) 100%),
      linear-gradient(90deg,
        #a4a5a6 0%, #b8b9ba 8%, #a6a7a8 16%, #c6c7c8 26%, #b0b1b2 36%,
        #a9aaab 46%, #6f7072 56%, #8a8b8d 62%, #5c5d60 70%,
        #7b7c7e 78%, #585a5d 88%, #6c6d70 100%);
  }
  .photo--stone {
    background:
      linear-gradient(165deg, rgba(40,35,30,0) 0%, rgba(40,35,30,.3) 60%, rgba(40,35,30,.1) 100%),
      linear-gradient(90deg,
        #5d5b5b 0%, #6e6b6a 10%, #5a5858 18%, #77736f 28%, #63605f 38%,
        #847d74 48%, #b4a590 58%, #8d8173 64%, #c9b79d 72%,
        #9c8e7c 80%, #d3c3aa 90%, #bfae96 100%);
  }
  .photo--faint {
    background:
      linear-gradient(180deg, rgba(255,255,255,0) 0%, #ffffff 92%),
      linear-gradient(90deg,
        #eeeef1 0%, #f7f7f9 10%, #e9e9ec 20%, #f5f5f7 32%, #ebebee 44%,
        #f6f6f8 56%, #e8e8eb 68%, #f4f4f6 80%, #e6e6ea 90%, #f2f2f4 100%);
  }

  .brand {
    position: absolute; display: flex; align-items: center; gap: 8px;
    color: var(--white); font-size: 22px; font-weight: 400;
  }
  .brand__dot { width: 34px; height: 34px; border-radius: 50%; background: var(--white); }
  .brand--tl { left: 48px; top: 56px; }
  .brand--tr { right: 44px; top: 58px; }

  .cover-title { position: absolute; color: var(--white); font-weight: 400; font-size: 40px; line-height: 1.1; white-space: nowrap; }
  .cover-sub { position: absolute; color: var(--white); font-size: 12.5px; white-space: nowrap; }
  .cover-sub--bold { font-weight: 700; }

  .slide--1 .cover-title { left: 46px; top: 300px; }
  .slide--1 .cover-sub { left: 48px; top: 352px; }
  .slide--2 .cover-title { right: 36px; top: 300px; }
  .slide--2 .cover-sub { right: 36px; top: 352px; }
  .slide--3 .cover-title { left: 44px; top: 330px; }
  .slide--3 .cover-sub { left: 46px; top: 380px; }
  .slide--4 .cover-title { left: 58px; top: 292px; }
  .slide--4 .cover-sub { left: 302px; top: 342px; }

  .heading { position: absolute; left: 32px; top: 30px; color: var(--ink-blue); font-size: 28px; font-weight: 400; }

  .wheel { position: absolute; left: 248px; top: 78px; width: 360px; height: 360px; }

  .footer {
    position: absolute; left: 0; right: 0; bottom: 0; height: 28px;
    background: var(--navy); color: var(--white);
    display: flex; align-items: center; font-size: 11px;
  }
  .footer__brand { display: flex; align-items: center; gap: 5px; margin-left: 8px; font-size: 11px; }
  .footer__dot { width: 14px; height: 14px; border-radius: 50%; background: var(--white); }
  .footer__note { margin-left: auto; margin-right: 28px; }
  .footer__page { width: 38px; height: 100%; background: var(--gray); display: flex; align-items: center; justify-content: center; }

  .seg-label { font-family: "Gelasio", Georgia, serif; font-size: 9.5px; fill: var(--ink-blue); text-anchor: middle; }
</style>
</head>
<body>

<svg width="0" height="0" style="position:absolute" aria-hidden="true">
  <defs>
    <filter id="petal-shadow" x="-10%" y="-10%" width="120%" height="120%">
      <feDropShadow dx="0" dy="1" stdDeviation="2" flood-color="#000" flood-opacity=".18"/>
    </filter>
    <symbol id="difference-wheel" viewBox="0 0 340 340">
      <g fill="none" stroke="#ffffff" stroke-width="40" stroke-dasharray="108 565" filter="url(#petal-shadow)">
        <circle cx="170" cy="170" r="107" transform="rotate(-149 170 170)"/>
        <circle cx="170" cy="170" r="107" transform="rotate(-89 170 170)"/>
        <circle cx="170" cy="170" r="107" transform="rotate(-29 170 170)"/>
        <circle cx="170" cy="170" r="107" transform="rotate(31 170 170)"/>
        <circle cx="170" cy="170" r="107" transform="rotate(91 170 170)"/>
        <circle cx="170" cy="170" r="107" transform="rotate(151 170 170)"/>
      </g>
      <g fill="none" stroke-width="24" stroke-dasharray="69 371">
        <circle cx="170" cy="170" r="70" stroke="var(--bright)" transform="rotate(-148 170 170)"/>
        <circle cx="170" cy="170" r="70" stroke="var(--navy)" transform="rotate(-88 170 170)"/>
        <circle cx="170" cy="170" r="70" stroke="var(--royal)" transform="rotate(-28 170 170)"/>
        <circle cx="170" cy="170" r="70" stroke="var(--charcoal)" transform="rotate(32 170 170)"/>
        <circle cx="170" cy="170" r="70" stroke="var(--gray)" transform="rotate(92 170 170)"/>
        <circle cx="170" cy="170" r="70" stroke="var(--sky)" transform="rotate(152 170 170)"/>
      </g>
      <circle cx="170" cy="170" r="46" fill="#ffffff" filter="url(#petal-shadow)"/>
      <circle cx="170" cy="170" r="22" fill="var(--gray)"/>
      <g transform="rotate(-30 170 170)"><text class="seg-label" x="170" y="60">Transparent</text><text class="seg-label" x="170" y="71">Communication</text></g>
      <g transform="rotate(30 170 170)"><text class="seg-label" x="170" y="60">Experienced</text><text class="seg-label" x="170" y="71">Investors</text></g>
      <g transform="rotate(90 170 170)"><text class="seg-label" x="170" y="55">Independent</text><text class="seg-label" x="170" y="66">Portfolio</text><text class="seg-label" x="170" y="77">Construction</text></g>
      <g transform="rotate(-30 170 170)"><text class="seg-label" x="170" y="274">Sound Operational</text><text class="seg-label" x="170" y="285">Platform</text></g>
      <g transform="rotate(30 170 170)"><text class="seg-label" x="170" y="274">Proactive Total Fee</text><text class="seg-label" x="170" y="285">Management</text></g>
      <g transform="rotate(-90 170 170)"><text class="seg-label" x="170" y="60">Institutional</text><text class="seg-label" x="170" y="71">Research Process</text></g>
      <g fill="#ffffff" filter="url(#petal-shadow)">
        <circle cx="96" cy="42" r="11"/><circle cx="244" cy="42" r="11"/><circle cx="318" cy="170" r="11"/>
        <circle cx="244" cy="298" r="11"/><circle cx="96" cy="298" r="11"/><circle cx="22" cy="170" r="11"/>
      </g>
      <g fill="var(--bright)">
        <rect x="90" y="37" width="12" height="8" rx="3"/><path d="M93 45 l-2 4 l5 -4z"/>
        <circle cx="244" cy="38" r="2.5"/><circle cx="240" cy="44" r="2.5"/><circle cx="248" cy="44" r="2.5"/>
        <path d="M313 165 h8 l3 3 v8 h-11z"/>
        <circle cx="19" cy="168" r="3"/><circle cx="25" cy="173" r="2.5"/>
      </g>
      <g fill="none" stroke="var(--charcoal)" stroke-width="1.6">
        <circle cx="244" cy="298" r="4.5"/><circle cx="244" cy="298" r="1.5"/>
        <rect x="89" y="295" width="14" height="6" rx="3"/>
      </g>
    </symbol>
  </defs>
</svg>

<section class="slide slide--1">
  <div class="photo photo--blue" role="img" aria-label="Blue-tinted photograph of a long colonnade with column shadows across the floor"></div>
  <div class="brand brand--tl"><span class="brand__dot"></span>Pelmar Capital Wealth</div>
  <h1 class="cover-title">Your Title Goes Here</h1>
  <p class="cover-sub cover-sub--bold">Pelmar Capital Wealth is an investment advisor founded by investors.</p>
</section>

<section class="slide slide--2">
  <div class="photo photo--royal" role="img" aria-label="Royal blue photograph of marble columns in a hall"></div>
  <div class="brand brand--tr"><span class="brand__dot"></span>Pelmar Capital Wealth</div>
  <h1 class="cover-title">Your Title Goes Here</h1>
  <p class="cover-sub cover-sub--bold">Pelmar Capital Wealth is an investment advisor founded by investors.</p>
</section>

<section class="slide slide--3">
  <div class="photo photo--gray" role="img" aria-label="Grey-toned photograph of columns reflected on a polished floor"></div>
  <div class="brand brand--tl"><span class="brand__dot"></span>Pelmar Capital Wealth</div>
  <h1 class="cover-title">Your Title Goes Here</h1>
  <p class="cover-sub">Your Subtitle Here</p>
</section>

<section class="slide slide--4">
  <div class="photo photo--stone" role="img" aria-label="Photograph of a sunlit stone colonnade with striped shadows on paving"></div>
  <div class="brand brand--tl"><span class="brand__dot"></span>Pelmar Capital Wealth</div>
  <h1 class="cover-title">Your Title Goes Here</h1>
  <p class="cover-sub">Your Subtitle Here</p>
</section>

<section class="slide slide--5">
  <div class="photo photo--faint" role="img" aria-label="Faded light photograph of white columns"></div>
  <h2 class="heading">The Pelmar Difference</h2>
  <svg class="wheel" viewBox="0 0 340 340" aria-label="Six differentiating factors"><use href="#difference-wheel"/></svg>
  <footer class="footer">
    <span class="footer__brand"><span class="footer__dot"></span>Pelmar</span>
    <span class="footer__note">Pelmar Capital Wealth is an investment advisor founded by investors.</span>
    <span class="footer__page">5</span>
  </footer>
</section>

<section class="slide slide--6" style="background:#fff">
  <h2 class="heading">The Pelmar Difference</h2>
  <svg class="wheel" viewBox="0 0 340 340" aria-label="Six differentiating factors"><use href="#difference-wheel"/></svg>
  <footer class="footer">
    <span class="footer__brand"><span class="footer__dot"></span>Pelmar</span>
    <span class="footer__note">Pelmar Capital Wealth is an investment advisor founded by investors.</span>
    <span class="footer__page">6</span>
  </footer>
</section>

</body>
</html>
```